International pain relief company needs flyer designed

We are based in South Australia, and are about to launch a brand new hand held portable fully chargeable pain relief device. This device gives the user proven instant relief often from the first time of use anywhere. We intend to offer, a try before you buy at home /office demonstration, a full 30 day money back guarantee and a full 3 year warranty. We also plan to give the first 7 people who book a demonstration a FREE $20 Bravon fuel card.
We are open minded regarding the overall design and colours used, however we are particularly keen on seeing pictures/cartoons of people suffering from the 3 main groups of pain, head ache, back ache and joint pain, perhaps also happy faces once they have been cured/relieved by our equipment. This product we expect to retail for around the $300 AUD mark.
The wording on the leaflet is
Suffering from headaches, back ache or joint problems?
At last....there is instant pain relief!
New to Australia, a personal portable pain relief device
Call Ned 0427580316 & 08 82947153
RMT Australia PO Box 628, Elmhurst SA 5093

Target Market(s)

aged, elderly

Industry/Entity Type

Retail

Font styles to use
Serif
Sans Serif

Colors
33b7a4
33a6d7
3176b5

Requirements
Must have
• include Free in house/office demonstration
Free $20 Bravon fuel card for first 11 demonstrations
Nice to have
• Bravon fuel logo

```html
<!DOCTYPE html>
<html lang="en">
<head>
<meta charset="utf-8">
<title>Bravon Pain Relief Flyer</title>
<link rel="stylesheet" href="https://fonts.googleapis.com/css2?family=Lato:wght@400;700&family=Teko:wght@400;500&display=swap">
<style>
  :root {
    --backdrop: #2e2f31;
    --paper: #ffffff;
    --teal-dark: #185f74;
    --teal: #1f7790;
    --teal-light: #2e91aa;
    --red: #e3222e;
    --ink: #1e1e1e;
    --logo-navy: #1f5f73;
  }
  * { box-sizing: border-box; margin: 0; padding: 0; }
  html, body { width: 896px; height: 1200px; overflow: hidden; }
  body { background: var(--backdrop); font-family: "Lato", sans-serif; position: relative; }

  .flyer {
    position: absolute; left: 70px; top: 60px; width: 762px; height: 1045px;
    background: var(--paper); overflow: hidden;
  }
  .hero-photo {
    position: absolute; left: 0; top: 0; width: 762px; height: 440px;
    background: linear-gradient(100deg, #7cc3d8 0%, #8fcbe0 28%, #a7c6a6 55%, #8fb06d 75%, #c9ddf0 100%);
  }
  .brand-tab {
    position: absolute; left: 230px; top: 0; width: 328px; height: 115px;
    background: var(--paper); border-radius: 0 0 22px 22px;
    display: flex; align-items: center; justify-content: center; gap: 16px;
  }
  .brand-dot { width: 56px; height: 56px; border-radius: 50%; background: var(--logo-navy); }
  .brand-name { font-family: "Lato", sans-serif; font-weight: 700; font-size: 38px; color: var(--logo-navy); letter-spacing: 1px; }

  .callout {
    position: absolute; right: 0; font-weight: 700; font-size: 14px; line-height: 1.25;
    border-radius: 18px 0 0 18px; padding: 8px 18px 8px 22px;
  }
  .callout--red { top: 150px; width: 357px; background: var(--red); color: #fff; }
  .callout--white { top: 240px; width: 328px; background: #fff; color: var(--ink); }

  .panel-curve { position: absolute; left: 0; top: 350px; width: 762px; height: 200px; }
  .offer {
    position: absolute; left: 0; width: 762px; top: 412px; text-align: center; color: #fff;
    font-weight: 700; font-size: 17px; line-height: 1.15;
  }
  .offer strong { font-size: 21px; }

  .panel {
    position: absolute; left: 0; top: 540px; width: 762px; height: 448px;
    background: radial-gradient(ellipse at 50% 40%, var(--teal-light) 0%, var(--teal) 55%, var(--teal-dark) 100%);
    border-radius: 0 0 36px 36px;
  }
  .headline {
    position: absolute; left: 0; width: 762px; top: 522px; text-align: center; color: #fff;
    font-family: "Teko", sans-serif; font-weight: 500; font-size: 37px; line-height: 38px;
    text-transform: uppercase; white-space: nowrap;
  }
  .pain-types { position: absolute; left: 0; top: 632px; width: 762px; }
  .pain-item { position: absolute; width: 200px; text-align: center; color: #fff; }
  .pain-item:nth-child(1) { left: 50px; }
  .pain-item:nth-child(2) { left: 297px; }
  .pain-item:nth-child(3) { left: 527px; }
  .pain-photo {
    display: block; margin: 0 auto; width: 144px; height: 144px; border-radius: 50%;
    border: 5px solid #fff; box-shadow: 0 0 0 2px rgba(255,255,255,0.25);
  }
  .pain-photo--head { background: linear-gradient(160deg, #e9d7c6, #c9a98a); }
  .pain-photo--back { background: linear-gradient(160deg, #8ab7cf, #9aa77e 60%, #5b6a7a); }
  .pain-photo--joint { background: linear-gradient(160deg, #9ed3ea, #d9a88d 55%, #e86a9c); }
  .pain-label { display: block; margin-top: 24px; font-weight: 700; font-size: 23px; }

  .intro {
    position: absolute; left: 0; width: 762px; top: 862px; text-align: center; color: #fff;
    font-family: "Teko", sans-serif; text-transform: uppercase; white-space: nowrap;
  }
  .intro-title { font-weight: 500; font-size: 35px; line-height: 36px; }
  .intro-body { font-size: 21px; line-height: 26px; margin-top: 2px; }

  .contact {
    position: absolute; left: 0; width: 762px; top: 990px; text-align: center; color: var(--ink);
  }
  .contact-line { display: flex; justify-content: center; align-items: center; gap: 8px; font-weight: 700; font-size: 22px; }
  .contact-name { margin-right: 26px; }
  .phone-icon { width: 22px; height: 22px; }
  .contact-gap { margin-left: 16px; }
  .contact-address { font-size: 15px; margin-top: 2px; }
</style>
</head>
<body>
  <article class="flyer">
    <div class="hero-photo" role="img" aria-label="Photo of a woman in a sports top holding her lower back in pain, outdoors"></div>

    <div class="brand-tab">
      <span class="brand-dot"></span>
      <span class="brand-name">BRAVON</span>
    </div>

    <p class="callout callout--red">We are based in South Australia, and are about to launch a brand new hand held portable fully chargeable pain relief device.</p>
    <p class="callout callout--white">This device gives the user proven instant relief often from the first time of use anywhere.</p>

    <svg class="panel-curve" viewBox="0 0 762 200" aria-hidden="true">
      <path d="M0 70 Q381 -30 762 70 L762 200 L0 200 Z" fill="#ffffff"/>
      <path d="M0 84 Q381 -12 762 84" fill="none" stroke="#e3222e" stroke-width="4"/>
      <path d="M0 96 Q381 6 762 96 L762 150 Q381 130 0 150 Z" fill="#e3222e"/>
      <path d="M0 150 Q381 130 762 150 L762 200 L0 200 Z" fill="#185f74"/>
      <path d="M0 156 Q381 136 762 156" fill="none" stroke="#ffffff" stroke-width="2"/>
    </svg>
    <p class="offer">Free in house/office demonstration<br><strong>$20</strong> Bravon fuel card for first<br>11 demonstrations</p>

    <div class="panel"></div>
    <h1 class="headline">Suffering from headaches, back ache or joint problems?<br>At last....there is instant pain relief!</h1>

    <div class="pain-types">
      <div class="pain-item">
        <span class="pain-photo pain-photo--head" role="img" aria-label="Photo of a woman holding her head with a headache"></span>
        <span class="pain-label">Head ache</span>
      </div>
      <div class="pain-item">
        <span class="pain-photo pain-photo--back" role="img" aria-label="Photo of a runner holding a sore knee"></span>
        <span class="pain-label">Back ache</span>
      </div>
      <div class="pain-item">
        <span class="pain-photo pain-photo--joint" role="img" aria-label="Photo of a woman holding her lower back"></span>
        <span class="pain-label">Joint pain</span>
      </div>
    </div>

    <div class="intro">
      <h2 class="intro-title">New to Australia, a personal portable pain relief device</h2>
      <p class="intro-body">We intend to offer, a try before you buy at home /office demonstration, a full 30 day<br>money back guarantee and a full 3 year warranty.</p>
    </div>

    <footer class="contact">
      <div class="contact-line">
        <span class="contact-name">Ned</span>
        <svg class="phone-icon" viewBox="0 0 22 22" aria-hidden="true"><rect width="22" height="22" rx="3" fill="#185f74"/><path d="M7 5 L9 5 L10 8 L8.5 9.5 Q10 12.5 12.5 13.5 L14 12 L17 13 L17 15 Q16 17 14 17 Q6 15 5 7 Q5 5 7 5 Z" fill="#fff"/></svg>
        <span>427580316 &amp; 08 82947153</span>
        <svg class="phone-icon contact-gap" viewBox="0 0 22 22" aria-hidden="true"><rect width="22" height="22" rx="3" fill="#185f74"/><path d="M7 5 L9 5 L10 8 L8.5 9.5 Q10 12.5 12.5 13.5 L14 12 L17 13 L17 15 Q16 17 14 17 Q6 15 5 7 Q5 5 7 5 Z" fill="#fff"/></svg>
        <span>(415) 555-0187</span>
      </div>
      <p class="contact-address">RMT Australia PO Box 628, Elmhurst SA 5093</p>
    </footer>
  </article>
</body>
</html>
```